Corvane spray foam and Environmental

I have business cards but need new ones. The ones I have are very bland. Here is. Y company website http://www.corvanesprayfoam.ca

Also I can send you copies of the current cards
I would also need my current logo on the new design as well.. Also spray foam and Environmental

Industry/Entity Type

Business

Logo Text

Corvane.

```html
<!DOCTYPE html>
<html lang="en">
<head>
<meta charset="utf-8">
<title>Corvane Spray Foam Ltd. – Business Cards</title>
<link rel="stylesheet" href="https://fonts.googleapis.com/css2?family=Jost:wght@400;500;600&display=swap">
<style>
  :root {
    --page: #2a2724;
    --card: #0b0b0c;
    --card-sheen: #2b2b2e;
    --purple: #9276c4;
    --purple-soft: #a893d4;
    --green: #5fc35a;
    --white: #f2f2f2;
    --font: "Jost", "Century Gothic", sans-serif;
  }
  * { box-sizing: border-box; margin: 0; padding: 0; }
  html, body { width: 1200px; height: 1200px; overflow: hidden; }
  body {
    background: var(--page);
    font-family: var(--font);
    display: flex;
    flex-direction: column;
    align-items: center;
    justify-content: space-evenly;
  }
  .card {
    position: relative;
    width: 840px;
    height: 480px;
    border-radius: 6px;
    overflow: hidden;
    background:
      radial-gradient(ellipse 60% 90% at 45% 35%, var(--card-sheen) 0%, transparent 70%),
      var(--card);
    box-shadow: 0 14px 30px rgba(0,0,0,.45);
  }

  /* ---------- front ---------- */
  .swoosh { position: absolute; inset: 0; width: 100%; height: 100%; }
  .brand {
    position: absolute;
    display: flex;
    align-items: center;
    gap: 20px;
  }
  .brand-mark {
    width: 96px; height: 96px;
    border-radius: 12px;
    background: linear-gradient(150deg, #6b4c9e, #3a3a46);
  }
  .brand-name {
    color: var(--white);
    font-weight: 500;
    letter-spacing: .06em;
    text-transform: uppercase;
    line-height: 1.05;
  }
  .front .brand { left: 46px; top: 100px; }
  .front .brand-name { font-size: 42px; }
  .front .brand-name small { display: block; font-size: 18px; letter-spacing: .1em; margin-top: 4px; }

  .services {
    position: absolute;
    right: 44px;
    text-align: right;
    text-transform: uppercase;
    font-weight: 500;
  }
  .services h2 { font-size: 24px; font-weight: 600; letter-spacing: .03em; line-height: 1.3; }
  .services p { font-size: 14px; letter-spacing: .03em; line-height: 1.45; }
  .services.spray { top: 226px; color: var(--purple); }
  .services.enviro { top: 338px; color: var(--green); }

  /* ---------- back ---------- */
  .back .brand {
    left: 50%; top: 50px;
    transform: translateX(-50%);
    flex-direction: column;
    gap: 12px;
    text-align: center;
  }
  .back .brand-mark { width: 84px; height: 84px; }
  .back .brand-name { font-size: 36px; }
  .back .brand-name small { display: block; font-size: 15px; letter-spacing: .1em; margin-top: 2px; }

  .contact {
    position: absolute;
    top: 238px;
    font-size: 16px;
    line-height: 1.6;
  }
  .contact .person { font-size: 14px; letter-spacing: .16em; text-transform: uppercase; font-weight: 600; }
  .contact .division { font-size: 22px; letter-spacing: .12em; text-transform: uppercase; font-weight: 600; line-height: 1.1; margin-bottom: 8px; }
  .contact ul { list-style: none; }
  .contact li { display: flex; align-items: center; gap: 10px; }
  .contact svg { width: 16px; height: 16px; flex: none; }
  .contact.spray { left: 46px; color: var(--purple-soft); }
  .contact.enviro { right: 46px; color: var(--green); text-align: right; }
  .contact.enviro li { justify-content: flex-end; }

  .address {
    position: absolute;
    left: 0; right: 0; bottom: 40px;
    text-align: center;
    color: var(--white);
    font-size: 19px;
    letter-spacing: .04em;
  }
</style>
</head>
<body>

<svg width="0" height="0" style="position:absolute" aria-hidden="true">
  <defs>
    <linearGradient id="swoosh-fill" x1="0" y1="1" x2="1" y2="0">
      <stop offset="0" stop-color="#5fc35a"/>
      <stop offset=".5" stop-color="#7f9a9a"/>
      <stop offset="1" stop-color="#9276c4"/>
    </linearGradient>
    <symbol id="icon-phone" viewBox="0 0 24 24"><path fill="currentColor" d="M6.6 10.8a15 15 0 0 0 6.6 6.6l2.2-2.2a1 1 0 0 1 1-.25 11.4 11.4 0 0 0 3.6.57 1 1 0 0 1 1 1V20a1 1 0 0 1-1 1A17 17 0 0 1 3 4a1 1 0 0 1 1-1h3.5a1 1 0 0 1 1 1c0 1.25.2 2.45.57 3.57a1 1 0 0 1-.25 1z"/></symbol>
    <symbol id="icon-mail" viewBox="0 0 24 24"><path fill="currentColor" d="M2 5h20v14H2zm2 2v.5l8 5 8-5V7l-8 5z"/></symbol>
    <symbol id="icon-web" viewBox="0 0 24 24"><g fill="none" stroke="currentColor" stroke-width="1.8"><circle cx="12" cy="12" r="9.5"/><ellipse cx="12" cy="12" rx="4.2" ry="9.5"/><path d="M2.5 12h19M4 7h16M4 17h16"/></g></symbol>
  </defs>
</svg>

<section class="card front" aria-label="Business card front">
  <svg class="swoosh" viewBox="0 0 840 480" preserveAspectRatio="none" aria-hidden="true">
    <path d="M0 440 C 180 470, 330 400, 400 262 S 520 30, 600 -10" fill="none" stroke="url(#swoosh-fill)" stroke-width="6"/>
  </svg>

  <div class="brand">
    <div class="brand-mark"></div>
    <p class="brand-name">Corvane<small>Spray Foam Ltd.</small></p>
  </div>

  <div class="services spray">
    <h2>Spray Foam</h2>
    <p>Roofing Foam · Slabjacking<br>2 Pound / Half Pound · Sound Proofing<br>Batt Insulation · Attic Blow In</p>
  </div>

  <div class="services enviro">
    <h2>Environmental</h2>
    <p>Air Monitoring · Asbestos Testing<br>Asbestos Removal · Building Demolition<br>Lead Testing · Mould Removal</p>
  </div>
</section>

<section class="card back" aria-label="Business card back">
  <div class="brand">
    <div class="brand-mark"></div>
    <p class="brand-name">Corvane<small>Spray Foam Ltd.</small></p>
  </div>

  <div class="contact spray">
    <p class="person">Marlow</p>
    <p class="division">Spray Foam</p>
    <ul>
      <li><svg><use href="#icon-phone"/></svg>604-555-0142</li>
      <li><svg><use href="#icon-mail"/></svg>corvanesprayfoam@mailbox.ca</li>
      <li><svg><use href="#icon-web"/></svg>www.corvanesprayfoam.ca</li>
    </ul>
  </div>

  <div class="contact enviro">
    <p class="person">Dorian</p>
    <p class="division">Environmental</p>
    <ul>
      <li>604-555-0187<svg><use href="#icon-phone"/></svg></li>
      <li>corvaneenviro1@mailbox.ca<svg><use href="#icon-mail"/></svg></li>
      <li>www.corvaneenvironmental.ca<svg><use href="#icon-web"/></svg></li>
    </ul>
  </div>

  <p class="address">4180 Larchmont Way Burnaby, BC.</p>
</section>

</body>
</html>
```